Design a Mobile App for Landscape Businesses

This project is to design the first three screens for a mobile app for Landscape and Lawncare businesses. This app will serve as a directory for homeowners to locate landscape and lawn care businesses and for landscape businesses and contractors to run their business. See the attached PDF for more information and example
Here is the link to the description https://lnkshrt.example/q7Tz3K

Target Market(s)

Landscape and lawn care business, gardeners, home owners

Industry/Entity Type

Landscape Gardening

Logo Text

Velmarigo

Colors

Designer to choose colors to be used in the design.

```html
<!DOCTYPE html>
<html lang="en">
<head>
<meta charset="utf-8">
<title>Velmarigo – Directory Screen</title>
<link href="https://fonts.googleapis.com/css2?family=Montserrat:wght@400;500;600;700&display=swap" rel="stylesheet">
<style>
  :root{
    --canvas:#3a3a3c;
    --screen-bg:#f1f1f3;
    --card:#ffffff;
    --ink:#1e1e22;
    --muted:#9a9aa2;
    --header-top:#cdd9a6;
    --header-mid:#8fd6d0;
    --header-bottom:#3bbcf2;
    --call:#8ed3c8;
    --link:#4aaee6;
    --tag-irrigation:#f27aa0;
    --tag-gardeners:#6ddc9c;
    --tag-landscape:#f9d27c;
    --tag-contractor:#36b4ee;
  }
  *{box-sizing:border-box;margin:0;padding:0}
  html,body{width:1200px;height:1200px;overflow:hidden}
  body{background:var(--canvas);font-family:"Montserrat",sans-serif;color:var(--ink);position:relative}
  .screen{position:absolute;left:330px;top:30px;width:540px;height:1140px;border-radius:48px;overflow:hidden;background:var(--screen-bg)}
  .app-header{height:250px;background:linear-gradient(160deg,var(--header-top) 0%,var(--header-mid) 45%,var(--header-bottom) 100%);position:relative;color:#fff}
  .status-bar{display:flex;justify-content:space-between;align-items:center;padding:22px 34px 0}
  .status-bar svg{display:block}
  .status-icons{display:flex;gap:10px}
  .toolbar{display:flex;justify-content:space-between;align-items:center;padding:26px 30px 0}
  .app-title{font-size:30px;font-weight:500;letter-spacing:.5px}
  .search-bar{position:absolute;left:24px;right:24px;bottom:-28px;height:62px;background:#fff;border-radius:6px;box-shadow:0 6px 18px rgba(0,0,0,.08);display:flex;align-items:center;gap:16px;padding:0 24px;color:var(--ink);font-size:17px}
  .results-count{margin:50px 24px 14px;font-size:11px;letter-spacing:1.4px;color:#b6b6bd;text-transform:uppercase}
  .listing{margin:0 18px 16px;background:var(--card);border-radius:6px;height:150px;display:flex;position:relative;box-shadow:0 3px 10px rgba(0,0,0,.04)}
  .listing-photo{width:150px;flex:none;border-radius:6px 0 0 6px}
  .listing-body{padding:18px 60px 0 18px}
  .tags{display:flex;gap:6px;margin-bottom:7px}
  .tag{font-size:8px;font-weight:600;letter-spacing:1px;color:#fff;text-transform:uppercase;padding:3px 8px;border-radius:10px}
  .tag--irrigation{background:var(--tag-irrigation)}
  .tag--gardeners{background:var(--tag-gardeners)}
  .tag--landscape{background:var(--tag-landscape)}
  .tag--contractor{background:var(--tag-contractor)}
  .listing-name{font-size:17px;font-weight:700;margin-bottom:6px}
  .listing-desc{font-size:10.5px;line-height:1.45;color:var(--muted)}
  .request-quote{display:inline-block;margin-top:8px;font-size:9.5px;font-weight:600;letter-spacing:1.6px;color:var(--link)}
  .call-button{position:absolute;top:14px;right:14px;width:40px;height:30px;border-radius:5px;background:var(--call);display:flex;align-items:center;justify-content:center}
</style>
</head>
<body>
<main class="screen">
  <header class="app-header">
    <div class="status-bar">
      <div class="status-icons">
        <svg width="18" height="14" viewBox="0 0 18 14" aria-hidden="true"><rect x="0" y="9" width="3" height="5" fill="#fff"/><rect x="5" y="6" width="3" height="8" fill="#fff"/><rect x="10" y="3" width="3" height="11" fill="#fff"/><rect x="15" y="0" width="3" height="14" fill="#fff"/></svg>
        <svg width="14" height="14" viewBox="0 0 14 14" aria-hidden="true"><circle cx="7" cy="7" r="6" fill="none" stroke="#fff" stroke-width="2"/><path d="M4 8l5-4-2 6z" fill="#fff"/></svg>
      </div>
      <div class="status-icons">
        <svg width="18" height="14" viewBox="0 0 18 14" aria-hidden="true"><path d="M1 5a12 12 0 0 1 16 0M4 8a7.5 7.5 0 0 1 10 0" fill="none" stroke="#fff" stroke-width="2"/><circle cx="9" cy="12" r="1.6" fill="#fff"/></svg>
        <svg width="26" height="14" viewBox="0 0 26 14" aria-hidden="true"><rect x="1" y="1" width="21" height="12" rx="2" fill="none" stroke="#fff" stroke-width="1.5"/><rect x="3" y="3" width="17" height="8" fill="#fff"/><rect x="23" y="5" width="2" height="4" fill="#fff"/></svg>
      </div>
    </div>
    <div class="toolbar">
      <svg width="26" height="20" viewBox="0 0 26 20" aria-label="Menu"><path d="M2 3h22M6 9h18M10 15h14" stroke="#fff" stroke-width="2" stroke-linecap="round"/></svg>
      <h1 class="app-title">Velmarigo</h1>
      <svg width="24" height="20" viewBox="0 0 24 20" aria-label="Filter"><path d="M1 1h22l-9 9v8l-4-2v-6z" fill="#fff"/></svg>
    </div>
    <div class="search-bar">
      <svg width="16" height="20" viewBox="0 0 16 20" aria-hidden="true"><path d="M8 0a8 8 0 0 1 8 8c0 6-8 12-8 12S0 14 0 8a8 8 0 0 1 8-8z" fill="#d8d8dd"/><circle cx="8" cy="8" r="3" fill="#fff"/></svg>
      <span>San Diego, CA</span>
    </div>
  </header>

  <p class="results-count">Showing 24 results</p>

  <section class="listings">
    <article class="listing">
      <div class="listing-photo" role="img" aria-label="Photo of sunlit lawn with trees" style="background:linear-gradient(160deg,#d9d2c0,#8c8a62 60%,#5b6b3a)"></div>
      <div class="listing-body">
        <div class="tags"><span class="tag tag--landscape">Landscape</span><span class="tag tag--gardeners">Gardeners</span></div>
        <h2 class="listing-name">Brightfield Lawn</h2>
        <p class="listing-desc">Lorem Ipsum is simply dummy text of the printing and typesetting industry. Lorem Ipsum has been the industry's standard dummy text</p>
        <span class="request-quote">REQUEST QUOTE →</span>
      </div>
      <div class="call-button"><svg width="16" height="16" viewBox="0 0 24 24" aria-label="Call"><path d="M6.6 10.8a15 15 0 0 0 6.6 6.6l2.2-2.2a1 1 0 0 1 1-.25 11.4 11.4 0 0 0 3.6.57 1 1 0 0 1 1 1V20a1 1 0 0 1-1 1A17 17 0 0 1 3 4a1 1 0 0 1 1-1h3.5a1 1 0 0 1 1 1c0 1.25.2 2.45.57 3.57a1 1 0 0 1-.25 1z" fill="#fff"/></svg></div>
    </article>

    <article class="listing">
      <div class="listing-photo" role="img" aria-label="Photo of red and yellow tulips" style="background:linear-gradient(160deg,#7e8f9c,#d9484f 50%,#5f8a3a)"></div>
      <div class="listing-body">
        <div class="tags"><span class="tag tag--irrigation">Irrigation</span><span class="tag tag--gardeners">Gardeners</span></div>
        <h2 class="listing-name">Greenmere</h2>
        <p class="listing-desc">Lorem Ipsum is simply dummy text of the printing and typesetting industry. Lorem Ipsum has been the industry's standard dummy text</p>
        <span class="request-quote">REQUEST QUOTE →</span>
      </div>
      <div class="call-button"><svg width="16" height="16" viewBox="0 0 24 24" aria-label="Call"><path d="M6.6 10.8a15 15 0 0 0 6.6 6.6l2.2-2.2a1 1 0 0 1 1-.25 11.4 11.4 0 0 0 3.6.57 1 1 0 0 1 1 1V20a1 1 0 0 1-1 1A17 17 0 0 1 3 4a1 1 0 0 1 1-1h3.5a1 1 0 0 1 1 1c0 1.25.2 2.45.57 3.57a1 1 0 0 1-.25 1z" fill="#fff"/></svg></div>
    </article>

    <article class="listing">
      <div class="listing-photo" role="img" aria-label="Photo of white garden flowers in a pot" style="background:linear-gradient(160deg,#c9dd9a,#eef2e2 55%,#8fb35a)"></div>
      <div class="listing-body">
        <div class="tags"><span class="tag tag--irrigation">Irrigation</span></div>
        <h2 class="listing-name">Larkspur Designs</h2>
        <p class="listing-desc">Lorem Ipsum is simply dummy text of the printing and typesetting industry. Lorem Ipsum has been the industry's standard dummy text</p>
        <span class="request-quote">REQUEST QUOTE →</span>
      </div>
      <div class="call-button"><svg width="16" height="16" viewBox="0 0 24 24" aria-label="Call"><path d="M6.6 10.8a15 15 0 0 0 6.6 6.6l2.2-2.2a1 1 0 0 1 1-.25 11.4 11.4 0 0 0 3.6.57 1 1 0 0 1 1 1V20a1 1 0 0 1-1 1A17 17 0 0 1 3 4a1 1 0 0 1 1-1h3.5a1 1 0 0 1 1 1c0 1.25.2 2.45.57 3.57a1 1 0 0 1-.25 1z" fill="#fff"/></svg></div>
    </article>

    <article class="listing">
      <div class="listing-photo" role="img" aria-label="Photo of park bench on a garden path" style="background:linear-gradient(160deg,#6f9a3f,#4f6f2a 50%,#a08c78)"></div>
      <div class="listing-body">
        <div class="tags"><span class="tag tag--irrigation">Irrigation</span><span class="tag tag--contractor">Contractor</span><span class="tag tag--landscape">Landscape</span></div>
        <h2 class="listing-name">Copperleaf Landscaping</h2>
        <p class="listing-desc">Lorem Ipsum is simply dummy text of the printing and typesetting industry. Lorem Ipsum has been the industry's standard dummy text</p>
        <span class="request-quote">REQUEST QUOTE →</span>
      </div>
      <div class="call-button"><svg width="16" height="16" viewBox="0 0 24 24" aria-label="Call"><path d="M6.6 10.8a15 15 0 0 0 6.6 6.6l2.2-2.2a1 1 0 0 1 1-.25 11.4 11.4 0 0 0 3.6.57 1 1 0 0 1 1 1V20a1 1 0 0 1-1 1A17 17 0 0 1 3 4a1 1 0 0 1 1-1h3.5a1 1 0 0 1 1 1c0 1.25.2 2.45.57 3.57a1 1 0 0 1-.25 1z" fill="#fff"/></svg></div>
    </article>

    <article class="listing">
      <div class="listing-photo" role="img" aria-label="Photo of purple bellflowers" style="background:linear-gradient(160deg,#e9eef0,#a77fd9 50%,#7ca24e)"></div>
      <div class="listing-body">
        <div class="tags"><span class="tag tag--contractor">Contractor</span><span class="tag tag--landscape">Landscape</span></div>
        <h2 class="listing-name">Hollin's Landscaping</h2>
        <p class="listing-desc">Lorem Ipsum is simply dummy text of the printing and typesetting industry. Lorem Ipsum has been the industry's standard dummy text</p>
        <span class="request-quote">REQUEST QUOTE →</span>
      </div>
      <div class="call-button"><svg width="16" height="16" viewBox="0 0 24 24" aria-label="Call"><path d="M6.6 10.8a15 15 0 0 0 6.6 6.6l2.2-2.2a1 1 0 0 1 1-.25 11.4 11.4 0 0 0 3.6.57 1 1 0 0 1 1 1V20a1 1 0 0 1-1 1A17 17 0 0 1 3 4a1 1 0 0 1 1-1h3.5a1 1 0 0 1 1 1c0 1.25.2 2.45.57 3.57a1 1 0 0 1-.25 1z" fill="#fff"/></svg></div>
    </article>
  </section>
</main>
</body>
</html>
```